International Travel Technology R&D business needs a wordpress website

We are a start up team of initially 2 individuals but plan to grow our team quickly, we have deep experience in travel technology. Our goal is to provide next generation technology research and development on behalf of our clients who are leading players in the travel technology industry. Attached our logos.

Target Market(s)

Travel Technology companies

Industry/Entity Type

Travel Industry

Coding

Coded - Design and coding required

Font styles to use
Sans Serif

Requirements
Must have
• Make use of our logo and colour scheme in the attached. Has to have a sense of adventure/ stepping into the unknown but equally must convey a sense of professionalism , we are a safe pair of hands. Sample themes are in the attachment .
Nice to have
• We have identified a theme on layoutgrove which we feel would be inspirational. We hahe attached them to help in the design as inspiration.
Should not have
• images of airplanes , hotels etc, we want to project a future image.

```html
<!DOCTYPE html>
<html lang="en">
<head>
<meta charset="utf-8">
<title>Travel Technology – Services</title>
<link rel="stylesheet" href="https://fonts.googleapis.com/css2?family=Open+Sans:wght@400;600&family=PT+Serif&family=Michroma&display=swap">
<style>
  :root {
    --accent: #27a9e1;
    --text: #666666;
    --heading: #1e1e1e;
    --page: #ffffff;
    --band: #efefef;
    --band-line: #d6d6d6;
    --partner: #3a6f9a;
    --footer: #282828;
    --footer-bottom: #1c1c1c;
    --footer-text: #8a8a8a;
    --footer-light: #e6e6e6;
  }
  * { box-sizing: border-box; margin: 0; padding: 0; }
  html, body { width: 1200px; height: 1200px; overflow: hidden; }
  body { background: var(--page); font-family: "Open Sans", sans-serif; position: relative; }

  .services { position: absolute; top: 0; left: 0; width: 1200px; height: 460px; }
  .service { position: absolute; top: 5px; width: 295px; text-align: center; }
  .service-photo { width: 295px; height: 208px; position: relative; overflow: hidden; }
  .service-photo::after { content: ""; position: absolute; left: 0; right: 0; bottom: 0; height: 40px; background: rgba(255,255,255,.18); }
  .photo-street { background: linear-gradient(160deg, #9a9a9a, #5c5c5c 55%, #b5b5b5); }
  .photo-tower { background: linear-gradient(180deg, #e4e6e8, #c4c9cc 60%, #9fb6c2); }
  .photo-facade { background: linear-gradient(120deg, #2b4a60, #4d6b80 50%, #1d3850); }
  .service-title { font-family: "PT Serif", serif; font-weight: 400; font-size: 17px; line-height: 22px; letter-spacing: .5px; color: var(--heading); margin-top: 26px; }
  .service-text { font-size: 12.2px; line-height: 17.6px; color: var(--text); margin: 10px auto 0; width: 275px; }
  .btn { display: inline-block; background: var(--accent); color: #fff; font-weight: 600; font-size: 12px; letter-spacing: 1px; text-transform: uppercase; border: none; }
  .service .btn { margin-top: 17px; width: 114px; height: 34px; line-height: 34px; }

  .partners { position: absolute; top: 460px; left: 0; width: 1200px; height: 343px; background: var(--band); }
  .partners-title { position: absolute; top: 56px; width: 100%; text-align: center; font-family: "Michroma", sans-serif; font-weight: 400; font-size: 25.5px; line-height: 36px; letter-spacing: 2px; color: var(--heading); }
  .partner-strip { position: absolute; top: 139px; left: 114px; width: 935px; height: 130px; border: 2px solid var(--band-line); display: flex; align-items: center; }
  .partner { flex: 1; height: 72px; display: flex; align-items: center; justify-content: center; gap: 7px; font-weight: 600; font-size: 16px; color: var(--partner); }
  .partner + .partner { border-left: 2px solid var(--band-line); }
  .partner-dot { width: 12px; height: 12px; border-radius: 50%; background: var(--accent); }

  .site-footer { position: absolute; top: 803px; left: 0; width: 1200px; height: 341px; background: var(--footer); }
  .footer-col { position: absolute; top: 62px; }
  .footer-col h3 { font-family: "PT Serif", serif; font-weight: 400; font-size: 19.5px; line-height: 24px; color: var(--footer-light); margin-bottom: 10px; white-space: nowrap; }
  .about { left: 112px; width: 210px; font-size: 10.5px; line-height: 17px; color: var(--footer-text); }
  .about .mail { margin-top: 17px; }
  .social { display: flex; gap: 19px; margin-top: 44px; }
  .social span { width: 14px; height: 14px; border-radius: 50%; background: #9a9a9a; }
  .news { left: 353px; width: 260px; font-size: 12px; line-height: 17px; }
  .news-item { margin-bottom: 16px; }
  .news-item strong { display: block; font-weight: 400; color: var(--footer-light); }
  .news-item p { color: var(--footer-text); }
  .links { left: 631px; font-size: 11.8px; line-height: 16.8px; color: var(--footer-text); }
  .links ul { list-style: none; }
  .contact { left: 833px; width: 217px; }
  .field { display: block; width: 217px; background: #fff; border: none; font-size: 10px; letter-spacing: .8px; color: #888; padding: 0 15px; }
  .field-email { height: 27px; line-height: 27px; margin-top: 5px; }
  .field-text { height: 67px; margin-top: 16px; padding-top: 6px; line-height: 16px; }
  .contact .btn { margin-top: 17px; width: 111px; height: 26px; line-height: 26px; font-weight: 400; font-size: 10px; letter-spacing: .6px; text-align: center; }

  .copyright { position: absolute; top: 1144px; left: 0; width: 1200px; height: 56px; background: var(--footer-bottom); text-align: center; line-height: 56px; font-size: 12px; color: #7a7a7a; }
</style>
</head>
<body>
  <section class="services">
    <article class="service" style="left:113px">
      <div class="service-photo photo-street" role="img" aria-label="Person with umbrella crossing a rainy city street"></div>
      <h2 class="service-title">NOSTRUD EXERCITATION</h2>
      <p class="service-text">Sed do eiusmod tempor incididunt ut labore et dolore magna aliqua. Ut enim ad minim veniam, quis nostrud exercitation ullamco laboris nisi ut aliquip ex ea commodo consequat.</p>
      <span class="btn">View More</span>
    </article>
    <article class="service" style="left:434px">
      <div class="service-photo photo-tower" role="img" aria-label="Hazy city skyline with a tall tower"></div>
      <h2 class="service-title">NOSTRUD EXERCITATION</h2>
      <p class="service-text">Sed do eiusmod tempor incididunt ut labore et dolore magna aliqua. Ut enim ad minim veniam, quis nostrud exercitation ullamco laboris nisi ut aliquip ex ea commodo consequat.</p>
      <span class="btn">View More</span>
    </article>
    <article class="service" style="left:753px">
      <div class="service-photo photo-facade" role="img" aria-label="Blue-toned stone building facade seen from below"></div>
      <h2 class="service-title">NOSTRUD EXERCITATION</h2>
      <p class="service-text">Sed do eiusmod tempor incididunt ut labore et dolore magna aliqua. Ut enim ad minim veniam, quis nostrud exercitation ullamco laboris nisi ut aliquip ex ea commodo consequat.</p>
      <span class="btn">View More</span>
    </article>
  </section>

  <section class="partners">
    <h2 class="partners-title">VOLUPTATE VELIT</h2>
    <div class="partner-strip">
      <div class="partner"><span class="partner-dot"></span>Bramblecot</div>
      <div class="partner">Quillmere</div>
      <div class="partner">Halden Group</div>
      <div class="partner">Orrin &amp; Pike</div>
      <div class="partner">Velmont</div>
    </div>
  </section>

  <footer class="site-footer">
    <div class="footer-col about">
      <h3>EIUSMOD TEMPOR</h3>
      <p>We would love to hear your stories and answer any questions you might have. Please drop us a line using any of these methods.</p>
      <p class="mail">E-mail: hello@novaroutelabs.com</p>
      <div class="social"><span></span><span></span><span></span><span></span><span></span></div>
    </div>
    <div class="footer-col news">
      <h3>EIUSMOD TEMPOR</h3>
      <div class="news-item"><strong>consectetur adipiscing elit</strong><p>Lorem ipsum dolor sit amet, consectetur adipiscing elit. Donec sed auctor elit.</p></div>
      <div class="news-item"><strong>consectetur adipiscing elit</strong><p>Lorem ipsum dolor sit amet, consectetur adipiscing elit. Donec sed auctor elit.</p></div>
      <div class="news-item"><strong>consectetur adipiscing elit</strong><p>Lorem ipsum dolor sit amet, consectetur adipiscing elit. Donec sed auctor elit.</p></div>
    </div>
    <div class="footer-col links">
      <h3>EIUSMOD TEMPOR</h3>
      <ul>
        <li>Consectetur</li><li>Adipiscsed do</li><li>Eiusmod tempor</li><li>Incididunt ut labore</li><li>Dolore magna</li><li>Aliquaad</li><li>Minim veniam, quis</li><li>Nostrud exercitation</li><li>Ullamco laboris nisi</li><li>Aliquip ex ea com-</li>
      </ul>
    </div>
    <div class="footer-col contact">
      <h3>CONTACT US</h3>
      <div class="field field-email">YOUR E-MAIL...</div>
      <div class="field field-text">YOUR TEXT...</div>
      <span class="btn">Send Message</span>
    </div>
  </footer>

  <div class="copyright">© Copyright 2016 Commodo consequat</div>
</body>
</html>
```